Business card for massage therapy company called Blue Fern Wellness

Need business card for massage therapy company called Blue Fern Wellness. Would like my logo on the front and the back of the card I have 3 options of logos and you can play with what looks better.

Would like this information displayed on the back of the card:

Marcus Ellery
Licensed Massage Therapist
415-903-2264
bluefern-wellness.example
bluefern_wellness_

```html
<!DOCTYPE html>
<html lang="en">
<head>
<meta charset="utf-8">
<title>Blue Fern Wellness – Business Card</title>
<link rel="stylesheet" href="https://fonts.googleapis.com/css2?family=Marcellus&family=Montserrat:wght@400;500;700&display=swap">
<style>
  :root {
    --stage: #2f2f31;
    --olive: #6d735c;
    --olive-dark: #5f6550;
    --tan: #c4916b;
    --paper: #ffffff;
    --ink: #3a3a36;
  }
  * { box-sizing: border-box; margin: 0; padding: 0; }
  html, body { width: 1200px; height: 915px; overflow: hidden; }
  body {
    background: var(--stage);
    display: flex; flex-direction: column; align-items: center; justify-content: center;
    gap: 60px;
    font-family: "Montserrat", sans-serif;
  }
  .card {
    position: relative; width: 600px; height: 343px;
    border-radius: 22px; overflow: hidden;
  }
  /* front */
  .card-front { background: var(--olive); }
  .front-pattern {
    position: absolute; inset: 0;
    background: radial-gradient(circle at 50% 50%, var(--olive) 0%, var(--olive-dark) 100%);
  }
  .front-logo {
    position: absolute; inset: 0;
    display: flex; align-items: center; justify-content: center; gap: 16px;
  }
  .logo-dot {
    width: 54px; height: 54px; border-radius: 50%;
    border: 2px solid var(--paper);
  }
  .front-name {
    font-family: "Marcellus", serif; font-size: 34px; line-height: 1.1;
    color: var(--paper); letter-spacing: 2px; text-transform: uppercase;
  }
  /* back */
  .card-back { background: var(--paper); }
  .back-wave { position: absolute; inset: 0; }
  .back-name {
    position: absolute; left: 40px; top: 52px;
    font-family: "Marcellus", serif; font-size: 38px; line-height: 1.05;
    color: var(--olive); letter-spacing: 2px; text-transform: uppercase;
  }
  .person {
    position: absolute; right: 40px; top: 72px; text-align: right;
  }
  .person-name {
    font-weight: 700; font-size: 21px; color: var(--olive); letter-spacing: 0.5px;
    text-transform: uppercase;
  }
  .person-role { font-size: 14px; color: var(--ink); margin-top: 4px; }
  .person-bar {
    position: absolute; right: 0; top: 66px; width: 16px; height: 54px;
    background: var(--tan);
  }
  .contacts {
    position: absolute; left: 40px; top: 170px; list-style: none;
    font-size: 15px; color: var(--ink);
  }
  .contacts li { display: flex; align-items: center; gap: 9px; height: 26px; }
  .contacts svg { width: 14px; height: 14px; flex: none; }
  .social-dot { width: 13px; height: 13px; border-radius: 50%; background: var(--tan); flex: none; }
</style>
</head>
<body>
  <section class="card card-front">
    <div class="front-pattern" role="img" aria-label="Repeating pattern of the brand mark on olive"></div>
    <div class="front-logo">
      <span class="logo-dot"></span>
      <p class="front-name">Blue Fern<br>Wellness</p>
    </div>
  </section>

  <section class="card card-back">
    <svg class="back-wave" viewBox="0 0 600 343" preserveAspectRatio="none">
      <path d="M0,292 C170,318 320,292 440,215 C510,172 560,158 600,154" fill="none" stroke="var(--tan)" stroke-width="5"/>
      <path d="M0,305 C170,330 330,305 450,228 C515,188 565,174 600,170 L600,343 L0,343 Z" fill="var(--olive)"/>
    </svg>
    <p class="back-name">Blue Fern<br>Wellness</p>
    <span class="person-bar"></span>
    <div class="person">
      <p class="person-name">Marcus Ellery</p>
      <p class="person-role">Licensed Massage Therapist</p>
    </div>
    <ul class="contacts">
      <li>
        <svg viewBox="0 0 24 24"><path d="M6.6 10.8a15 15 0 0 0 6.6 6.6l2.2-2.2c.3-.3.7-.4 1-.2 1.1.4 2.3.6 3.6.6.6 0 1 .4 1 1V20c0 .6-.4 1-1 1A17 17 0 0 1 3 4c0-.6.4-1 1-1h3.5c.6 0 1 .4 1 1 0 1.3.2 2.5.6 3.6.1.3 0 .7-.2 1z" fill="var(--tan)"/></svg>
        415-903-2264
      </li>
      <li>
        <svg viewBox="0 0 24 24"><rect x="2" y="5" width="20" height="14" rx="1" fill="var(--tan)"/><path d="M2 6l10 7 10-7" fill="none" stroke="#fff" stroke-width="1.6"/></svg>
        info@bluefern-wellness.example
      </li>
      <li>
        <svg viewBox="0 0 24 24" fill="none" stroke="var(--tan)" stroke-width="2"><circle cx="12" cy="12" r="9"/><path d="M3 12h18M12 3c3 3 3 15 0 18M12 3c-3 3-3 15 0 18"/></svg>
        www.bluefern-wellness.example
      </li>
      <li>
        <span class="social-dot"></span>
        @bluefern_wellness_
      </li>
    </ul>
  </section>
</body>
</html>
```